Poster design for "A Frame" Sign

I need a design for an A Frame sign. Measurements and Specifications here:
http://www.trimpaneldepot.com.au/pg/a-boards/XQRTMNDLW-Print-Specs.pdf

Actually, it will need to be two designs, one with an arrow pointing left and one with an arrow pointing right, otherwise exactly the same.

LOGO to be used is attached. Colours of design should match logo and should also include orange tones.

The A Frame sign is to be put on the driveway of my home studio at a main road in a residential suburban area. Cars drive by at around 50 km/h, so there needs to be an eye catcher that there is a nurturing home massage studio here.

Logo can be left or right, somehow incorporated into the text below:
-
[Big header, ideally "LeHavre" font]
Marindi Healing
Massage Studio

[slightly smaller font, serif, with bullet points]
- Relaxation Massage
- Remedial Massage
- Pregnancy Massage
- Kahuna Massage

[big Arrow to the left/right - one for each side of the frame]

[sans serif font, same size as above]
Bookings essential!
ph 0491 786 514
www.marindihealing.com.au

[serif font, same as above]
EFTPOS and instant health fund claims available.
-

Industry/Entity Type

Residential

Colors
f37022

```html
<!DOCTYPE html>
<html lang="en">
<head>
<meta charset="utf-8">
<title>Marindi Healing – A-Frame Poster</title>
<link rel="stylesheet" href="https://fonts.googleapis.com/css2?family=Great+Vibes&family=Old+Standard+TT:wght@400&display=swap">
<style>
  :root {
    --page: #f4f1ee;
    --sand: #d9ccbd;
    --plum: #9b2f72;
    --magenta: #e0197d;
    --ribbon: #d81b63;
    --ribbon-dark: #6d5a52;
    --orange: #f7ad3d;
    --paper: #f3ecdc;
    --paper-edge: #c9bda6;
    --wine: #7a1f3d;
    --circle: #e94a8f;
    --circle-ring: #8a1840;
    --white: #ffffff;
    --script: "Great Vibes", cursive;
    --serif: "Old Standard TT", serif;
  }
  * { box-sizing: border-box; margin: 0; padding: 0; }
  html, body { width: 1200px; height: 1074px; overflow: hidden; background: var(--page); }
  .poster {
    position: absolute; left: 250px; top: 20px;
    width: 700px; height: 1034px;
    background: var(--sand); overflow: hidden;
    font-family: var(--serif);
  }
  .poster__title {
    position: absolute; left: 0; top: 32px; width: 700px;
    text-align: center; font-family: var(--script); font-weight: 400;
    font-size: 96px; line-height: 1.1; color: var(--magenta);
    white-space: nowrap;
  }
  .poster__rule {
    position: absolute; left: 35px; top: 157px; width: 630px; height: 2px;
    background: var(--plum);
  }
  .poster__subtitle {
    position: absolute; left: 0; top: 164px; width: 700px;
    text-align: center; font-size: 52px; line-height: 1.2; color: var(--plum);
    letter-spacing: 1px; white-space: nowrap;
  }
  .brand-disc {
    position: absolute; left: 19px; top: 240px; width: 312px; height: 312px;
    border-radius: 50%; background: var(--circle);
    border: 14px solid var(--circle-ring);
    display: flex; align-items: center; justify-content: center;
  }
  .brand-disc__name { font-size: 34px; color: var(--white); white-space: nowrap; }
  .services { position: absolute; left: 340px; top: 320px; width: 330px; height: 490px; }
  .services__ribbon { position: absolute; left: 0; top: 0; }
  .services__label {
    position: absolute; left: 26px; top: 28px; width: 276px; height: 150px;
    background: var(--orange); border-radius: 46px;
    color: var(--white); font-size: 35px; line-height: 1.08;
    padding: 32px 0 0 46px;
  }
  .services__list { list-style: none; }
  .services__item {
    position: absolute; left: 6px; width: 310px; height: 52px;
    background: var(--paper); border-bottom: 2px dashed var(--paper-edge);
    box-shadow: 0 2px 3px rgba(0,0,0,.12);
    color: var(--wine); font-size: 26px; letter-spacing: .5px;
    text-align: center; line-height: 52px; white-space: nowrap;
  }
  .services__item:nth-child(1) { top: 177px; }
  .services__item:nth-child(2) { top: 243px; }
  .services__item:nth-child(3) { top: 309px; }
  .services__item:nth-child(4) { top: 376px; }
  .booking {
    position: absolute; left: 50px; top: 640px; width: 270px;
    transform: rotate(-12deg); transform-origin: left top;
  }
  .booking__line {
    background: var(--paper); border-bottom: 2px dashed #6b6158;
    color: var(--orange); padding: 8px 12px; white-space: nowrap;
  }
  .booking__line--head { font-size: 27px; letter-spacing: 1px; }
  .booking__line--phone { font-size: 27px; padding-left: 18px; display: flex; align-items: center; gap: 14px; letter-spacing: 1px; }
  .booking__line--web { font-size: 15px; padding: 18px 12px 14px 16px; border-bottom: none; letter-spacing: .5px; }
  .payment {
    position: absolute; left: 0; top: 882px; width: 700px;
    text-align: center; font-size: 25px; color: var(--magenta); letter-spacing: .6px;
    white-space: nowrap;
  }
  .direction-bar { position: absolute; left: 0; top: 936px; }
  .direction-bar__name {
    position: absolute; left: 155px; top: 956px;
    font-size: 30px; color: var(--white); white-space: nowrap;
  }
</style>
</head>
<body>
  <main class="poster">
    <h1 class="poster__title">Marindi Healing</h1>
    <div class="poster__rule"></div>
    <p class="poster__subtitle">MASSAGE STUDIO</p>

    <div class="brand-disc"><span class="brand-disc__name">Marindi Healing</span></div>

    <section class="services">
      <svg class="services__ribbon" width="330" height="490" viewBox="0 0 330 490">
        <path d="M74 6 H245 V486 L160 452 L74 486 Z" fill="var(--ribbon-dark)"/>
        <path d="M74 0 H245 V480 L160 446 L74 480 Z" fill="var(--ribbon)"/>
      </svg>
      <div class="services__label">MASSAGE<br>POSSIBLE:</div>
      <ul class="services__list">
        <li class="services__item">Relaxation Massage</li>
        <li class="services__item">Remedial Massage</li>
        <li class="services__item">Pregnancy Massage</li>
        <li class="services__item">Kahuna Massage</li>
      </ul>
    </section>

    <section class="booking">
      <p class="booking__line booking__line--head">Bookings essential!</p>
      <p class="booking__line booking__line--phone">
        <svg width="20" height="30" viewBox="0 0 20 30" aria-hidden="true"><path d="M6 2 L11 2 L11 9 L8 10 Q7 15 8 20 L11 21 L11 28 L6 28 Q1 15 6 2 Z" fill="var(--orange)"/></svg>
        0491 786 514
      </p>
      <p class="booking__line booking__line--web">www.marindihealing.com.au</p>
    </section>

    <p class="payment">EFTPOS and instant health fund claims available!</p>

    <svg class="direction-bar" width="700" height="98" viewBox="0 0 700 98">
      <defs>
        <linearGradient id="barFill" x1="0" x2="1">
          <stop offset="0" stop-color="var(--plum)"/>
          <stop offset="1" stop-color="var(--magenta)"/>
        </linearGradient>
      </defs>
      <path d="M0 10 H560 L585 46 L560 82 H0 Z" fill="#6a4a4e"/>
      <path d="M0 2 H552 L577 38 L552 74 H0 Z" fill="url(#barFill)"/>
      <circle cx="110" cy="38" r="26" fill="var(--white)"/>
      <g fill="none" stroke="var(--white)" stroke-width="6">
        <path d="M430 14 L454 38 L430 62"/>
        <path d="M450 14 L474 38 L450 62"/>
        <path d="M470 14 L494 38 L470 62"/>
        <path d="M490 14 L514 38 L490 62"/>
        <path d="M510 14 L534 38 L510 62"/>
      </g>
    </svg>
    <span class="direction-bar__name">Marindi Healing</span>
  </main>
</body>
</html>
```